THE Harrowfield Mobility Fund (HMF) PHOTOGRAPHY COMPETITION

We need a "flyer" (must be web friendly" as well as A5 Print) designed that will announce the launch of a new photography competition. The Theme of the Competition will be "Keep Moving Forward".

Harrowfield Mobility Fund will "host" a competition that is open to all comers, irrespective of experience, but within the following Classes : 1. People Living with Spinal Injuries 2. Schools 3. Amateur Under 18 Photographers 4. Amateur Over 18 Photographers 5. Charities 6. Professional Photographers.

The competition will start in October 2018 and entries will be accepted via the HMF website until 31st August 2019. Prizes to include a Cash Prize of £7,500 for the photograph that in the opinion of the judges best meets the brief. Each Class winner and runner up will receive photographic equipment (a camera for the winner, a tripod for the runner up). The two best photographs in each class will be included in HMF's 2020 Calendar. Prizes will be presented at an event in Salisbury in October 2019.

Entry Fee (payable via the HMF website) will be £2.00 per photograph.

Please note that this is an initial "draft" and any published "flyer / web page will have to meet current UK Charity Regulations.

Telephone +44 (0)1632 960418

www.hmf-example.org.uk (new website to be launched prior to Competition starting)

find us on facebook & twitter

Registered charity No. 1098472

Target Market(s)

Photographers, Schools, Charities

Industry/Entity Type

Charity

Font styles to use
Sans Serif

Colors

Designer to choose colors to be used in the design.

Requirements
Must have
• The HMF Logo
Nice to have
• Less words, high graphic appeal
Should not have
• Any doom and gloom! - People Living with Spinal Injuries are not "sick" - they are "Living With" Spinal Injury - not dieing from it!

```html
<!DOCTYPE html>
<html lang="en">
<head>
<meta charset="utf-8">
<title>Keep Moving Forward – Photography Competition</title>
<link rel="stylesheet" href="https://fonts.googleapis.com/css2?family=Oswald:wght@200;300&family=Montserrat:wght@600;700&family=Cormorant+Garamond:wght@500&display=swap">
<style>
  :root{
    --sun:#fbd67a;
    --sky:#72c4e9;
    --sky-deep:#4fa8d6;
    --white:#ffffff;
    --ink:#6b6a63;
    --steel-light:#9a9a9a;
    --steel-dark:#1d1d1d;
  }
  html,body{margin:0;padding:0;overflow:hidden;background:var(--sun);}
  .flyer{position:relative;width:846px;height:1200px;overflow:hidden;background:var(--sun);font-family:"Montserrat",sans-serif;}
  .backdrop{position:absolute;inset:0;width:846px;height:1200px;}
  .site-url{position:absolute;left:200px;top:46px;width:330px;color:var(--white);font-weight:700;font-size:12px;letter-spacing:5.2px;white-space:nowrap;}
  .logo-box{position:absolute;left:555px;top:46px;width:229px;height:161px;background:var(--white);display:flex;align-items:center;justify-content:center;gap:12px;}
  .logo-mark{width:14px;height:14px;border-radius:50%;background:var(--sky);flex:none;}
  .logo-name{font-family:"Cormorant Garamond",serif;font-weight:500;color:var(--ink);font-size:26px;line-height:25px;text-transform:uppercase;margin:0;}
  .camera-photo{position:absolute;left:78px;top:406px;width:515px;height:245px;border-radius:18px;transform:rotate(-36deg);
    background:linear-gradient(180deg,var(--steel-light) 0%,#d9d9d9 22%,#2a2a2a 30%,var(--steel-dark) 100%);
    box-shadow:40px 70px 60px rgba(40,70,100,.35);}
  .headline{position:absolute;left:560px;top:524px;width:480px;height:380px;transform:rotate(45deg);transform-origin:0 0;}
  .headline > *{position:absolute;margin:0;white-space:nowrap;}
  .kicker{left:0;top:0;font-family:"Oswald",sans-serif;font-weight:200;color:var(--white);font-size:28px;line-height:30px;letter-spacing:1px;text-transform:uppercase;}
  .title-lead{left:60px;top:18px;font-family:"Oswald",sans-serif;font-weight:300;color:var(--sun);font-size:170px;line-height:190px;letter-spacing:6px;text-transform:uppercase;}
  .title-band{left:0;top:206px;width:430px;height:80px;background:var(--white);font-family:"Oswald",sans-serif;font-weight:200;color:var(--sky-deep);font-size:52px;line-height:80px;text-align:center;text-transform:uppercase;letter-spacing:2px;overflow:hidden;}
  .open-call{left:11px;top:296px;color:var(--sun);font-weight:700;font-size:21px;letter-spacing:5px;text-transform:uppercase;}
  .dates{left:11px;color:var(--white);font-weight:600;font-size:17px;letter-spacing:9px;text-transform:uppercase;}
  .dates.from{top:330px;}
  .dates.to{top:358px;}
</style>
</head>
<body>
<main class="flyer">
  <svg class="backdrop" viewBox="0 0 846 1200" aria-hidden="true">
    <polygon points="846,240 846,1200 0,1200 0,1092" fill="var(--sky)"/>
    <line x1="850" y1="764" x2="412" y2="1204" stroke="var(--sun)" stroke-width="6"/>
  </svg>

  <div class="site-url">WWW.HMF-EXAMPLE.ORG.UK</div>

  <div class="logo-box">
    <span class="logo-mark"></span>
    <p class="logo-name">Harrowfield<br>Mobility<br>Fund</p>
  </div>

  <div class="camera-photo" role="img" aria-label="Photograph of a vintage silver and black rangefinder camera, tilted"></div>

  <section class="headline">
    <p class="kicker">Photography Competition</p>
    <p class="title-lead">Keep</p>
    <p class="title-band">Moving Forward</p>
    <p class="open-call">Open to all comers</p>
    <p class="dates from">From October 2018</p>
    <p class="dates to">To August 31, 2019</p>
  </section>
</main>
</body>
</html>
```